PELUNO soap beauty bar

I need a box designed to put a 4oz bar of soap inside. All sides of the box need design. A refreshingly fragrant blend of citrus and spicy notes, it is made with a blend of essential oils including ginger, mandarin, lemon and orange flowers

Target Market(s)

Homeless people

Requirements
Must have
• My company logo as pictured with text and design like a standard bar of soap. Weight 4oz, ingredients:
Olive oil, Coconut oil,Organic sustainable palm oil,Water,Lye,Shea butter, orange, ginger, mandarin, lemon essential oil. uploading pics for inspiration.
Nice to have
• The soap box measurements are Dimensions (L x W x H). 5.75 x 3.80 x 5.60 Inches ...

```html
<!DOCTYPE html>
<html lang="en">
<head>
<meta charset="utf-8">
<title>PELUNO Soap Beauty Bar – Box Panels</title>
<link href="https://fonts.googleapis.com/css2?family=Ubuntu:wght@400;500;700&display=swap" rel="stylesheet">
<style>
  :root {
    --bg: #c8dbe4;
    --leaf: #3f8f2a;
    --leaf-dark: #2f7420;
    --label-bg: #9cc79a;
    --label-ink: #3e6e52;
    --peach-top: #f3c79a;
    --peach-bottom: #eaa98a;
    --strip: #a6d39a;
    --strip-ink: #2d4f2a;
    --apple-red: #c4141c;
    --tag-bg: #b9dfb0;
  }
  * { box-sizing: border-box; margin: 0; padding: 0; }
  html, body { width: 1200px; height: 788px; overflow: hidden; }
  body {
    background: var(--bg);
    font-family: "Ubuntu", sans-serif;
    position: relative;
  }
  .box-panels {
    position: absolute;
    left: 150px;
    top: 154px;
    display: flex;
    height: 480px;
  }
  .front-panel {
    position: relative;
    width: 660px;
    height: 100%;
    overflow: hidden;
  }
  .fresh-backdrop {
    position: absolute;
    inset: 0 0 92px 0;
    background:
      radial-gradient(circle at 70% 55%, #f7f3b4 0%, rgba(247,243,180,0) 45%),
      linear-gradient(160deg, #a9d27a 0%, #d5e89a 45%, #eef0a8 70%, #b8d98a 100%);
  }
  .citrus-band {
    position: absolute;
    left: 0; right: 0; bottom: 0;
    height: 92px;
    background: linear-gradient(180deg, var(--peach-top), var(--peach-bottom));
  }
  .oils-strip {
    position: absolute;
    left: 0; right: 0; bottom: 0;
    height: 24px;
    background: var(--strip);
    color: var(--strip-ink);
    font-size: 11px;
    font-weight: 500;
    letter-spacing: 0.3px;
    display: flex;
    align-items: center;
    justify-content: center;
  }
  .weight-tag {
    position: absolute;
    right: 120px;
    bottom: 38px;
    background: var(--tag-bg);
    color: var(--strip-ink);
    font-size: 15px;
    font-weight: 500;
    padding: 5px 12px;
  }
  .brand-mark {
    position: absolute;
    left: 56px;
    top: 210px;
    display: flex;
    align-items: center;
    gap: 22px;
  }
  .brand-dot {
    width: 70px; height: 70px;
    border-radius: 50%;
    background: var(--apple-red);
  }
  .brand-name {
    font-size: 104px;
    font-weight: 700;
    color: var(--leaf);
    letter-spacing: 2px;
    line-height: 1;
  }
  .product-label {
    position: absolute;
    right: 34px;
    top: 54px;
    background: var(--label-bg);
    color: var(--label-ink);
    padding: 10px 18px 12px;
  }
  .product-label .title {
    font-size: 28px;
    font-weight: 500;
    letter-spacing: 0.5px;
  }
  .product-label .claim {
    font-size: 22px;
    font-weight: 400;
    margin-top: 2px;
  }
  .side-panel {
    position: relative;
    width: 190px;
    height: 100%;
    background: linear-gradient(180deg, #c4e09a 0%, #e4eca6 55%, #b7d88a 100%);
    overflow: hidden;
  }
  .side-band {
    position: absolute;
    left: 0; right: 0; bottom: 0;
    height: 92px;
    background: linear-gradient(180deg, var(--peach-top), var(--peach-bottom));
  }
  .side-dot {
    position: absolute;
    left: 68px; top: 40px;
    width: 54px; height: 54px;
    border-radius: 50%;
    background: var(--apple-red);
  }
  .side-name {
    position: absolute;
    left: 95px;
    top: 260px;
    transform: translate(-50%, -50%) rotate(90deg);
    font-size: 56px;
    font-weight: 700;
    color: var(--leaf);
    letter-spacing: 2px;
  }
</style>
</head>
<body>
  <main class="box-panels">
    <section class="front-panel">
      <div class="fresh-backdrop" role="img" aria-label="Soft green and yellow backdrop with water splash and bubbles"></div>
      <div class="product-label">
        <div class="title">SOAP BEAUTY BAR</div>
        <div class="claim">for soft, smooth skin</div>
      </div>
      <div class="brand-mark">
        <span class="brand-dot"></span>
        <span class="brand-name">PELUNO</span>
      </div>
      <div class="citrus-band"></div>
      <div class="weight-tag">Wt. 4 oz</div>
      <div class="oils-strip">MADE WITH A BLEND OF ESSENTIAL OILS INCLUDING GINGER, MANDARIN, LEMON AND ORANGE FLOWERS</div>
    </section>
    <section class="side-panel">
      <span class="side-dot"></span>
      <span class="side-name">PELUNO</span>
      <div class="side-band"></div>
    </section>
  </main>
</body>
</html>
```